Folded A4 flyer for design&construction company

Folded A4 flyer needed. Keywords: elegant, stylish
our website www.dravimo.ae

Industry/Entity Type

Construction

```html
<!DOCTYPE html>
<html lang="en">
<head>
<meta charset="utf-8">
<title>Dravimo – Design &amp; Construction Flyer</title>
<link rel="stylesheet" href="https://fonts.googleapis.com/css2?family=Lato:wght@300;400&display=swap">
<style>
  :root {
    --paper: #ffffff;
    --backdrop: #e9e9e9;
    --ink: #1a1a1a;
    --body-text: #7a7a7a;
    --muted: #c4c4c4;
    --grey-panel: #bdbdbd;
    --lime: #c3d62f;
    --sky: #00b4ea;
    --rose: #e35ba0;
    --sun: #fcc30e;
    --quote-lime: #d7e21a;
    --fitout-title: #e8e21c;
    --landscape-title: #f6c41b;
  }
  * { box-sizing: border-box; margin: 0; padding: 0; }
  html, body { width: 800px; height: 1200px; overflow: hidden; }
  body { background: var(--backdrop); font-family: "Lato", sans-serif; position: relative; }

  .spread { position: absolute; left: 63px; width: 674px; height: 476px; display: flex; box-shadow: 0 2px 8px rgba(0,0,0,.18); }
  .spread--outside { top: 114px; }
  .spread--inside { top: 610px; }
  .page { position: relative; width: 337px; height: 476px; overflow: hidden; background: var(--paper); }

  .wordmark { position: absolute; left: 0; right: 0; text-align: center; color: var(--ink); font-weight: 400; letter-spacing: 1px; line-height: 1; }

  /* back page */
  .back .wordmark { top: 90px; font-size: 34px; }
  .about { position: absolute; left: 54px; top: 148px; width: 229px; font-size: 8.4px; line-height: 11.6px; font-weight: 300; color: var(--body-text); text-align: justify; }
  .photo-strip { position: absolute; top: 257px; left: 0; width: 337px; height: 66px; display: flex; }
  .photo-strip .photo { height: 100%; }
  .photo--spa { width: 109px; background: linear-gradient(135deg, #d9b98c, #a8764a 60%, #e9d8bf); }
  .photo--lounge { width: 140px; background: linear-gradient(90deg, #e4d5bf, #8a6a4a 55%, #c79a66); }
  .photo--atrium { width: 88px; background: linear-gradient(160deg, #f3d08a, #e6a12c 55%, #b98855); }
  .contact-panel { position: absolute; top: 323px; left: 0; width: 337px; height: 153px; background: var(--grey-panel); }
  .quote-box { position: absolute; left: 77px; top: 17px; width: 182px; height: 62px; border: 1px solid #fff; text-align: center; color: #fff; font-size: 8px; line-height: 11.5px; padding-top: 6px; }
  .quote-box .cta { color: var(--quote-lime); font-size: 9.5px; margin-bottom: 1px; }
  .contact-panel .web { position: absolute; top: 97px; left: 0; right: 0; text-align: center; color: #fff; font-size: 8px; }
  .contact-panel .address { position: absolute; top: 111px; left: 54px; color: #fff; font-size: 8px; white-space: nowrap; }

  /* cover */
  .cover .wordmark { top: 84px; font-size: 44px; }
  .motto { position: absolute; top: 164px; left: 0; right: 0; text-align: center; color: var(--muted); font-weight: 300; font-size: 11.5px; letter-spacing: 1px; }
  .motto-source { position: absolute; top: 184px; left: 0; right: 0; text-align: center; color: var(--muted); font-weight: 300; font-size: 8.5px; letter-spacing: 1px; }
  .cover-photo { position: absolute; top: 198px; left: 0; width: 337px; height: 278px;
    background: linear-gradient(180deg, #ffffff 0%, #ebebea 22%, #dcdcda 48%, #f2f2f2 62%, #cfcfcf 78%, #e8e8e8 100%); }

  /* inside panels */
  .service { position: absolute; }
  .service-band { position: absolute; }
  .service-photo { position: absolute; }
  .badge { position: absolute; width: 69px; height: 52px; background: var(--paper); display: flex; align-items: center; justify-content: center; font-size: 15px; color: var(--ink); letter-spacing: .3px; }
  .service-title { position: absolute; font-size: 15.5px; font-weight: 400; white-space: nowrap; }
  .service-list { position: absolute; list-style: none; font-size: 9.2px; font-weight: 300; line-height: 14.6px; }
  .service-list--left { text-align: right; }
  .service-list--left li { padding-right: 25px; position: relative; }
  .service-list--left li::after { content: ""; position: absolute; right: 0; top: 7px; width: 19px; height: 1.6px; background: var(--ink); }
  .service-list--right li { padding-left: 26px; position: relative; }
  .service-list--right li.dash::before { content: ""; position: absolute; left: 0; top: 7px; width: 19px; height: 1.6px; background: var(--ink); }
  .service-list--light li::after { background: #fff; }
</style>
</head>
<body>

<section class="spread spread--outside">
  <div class="page back">
    <div class="wordmark">DRAVIMO</div>
    <p class="about">We believe in quality beginnings and flawless finishes. We are a team of creative designers and constructors with years of experience and expertise in providing complete interior design and construction services. Our unique designing prowess is complemented by our unflinching commitment to quality construction. Our team specializes in classic and contemporary high quality construction in Dubai for commercial and residential projects.</p>
    <div class="photo-strip">
      <div class="photo photo--spa" role="img" aria-label="Photo of a bathroom with an arched window and jacuzzi"></div>
      <div class="photo photo--lounge" role="img" aria-label="Photo of a living room with wooden wall panels"></div>
      <div class="photo photo--atrium" role="img" aria-label="Photo of a curved atrium with a spiral staircase"></div>
    </div>
    <div class="contact-panel">
      <div class="quote-box">
        <div class="cta">GET A FREE QUOTE TODAY!</div>
        <div>800 – DRAVIMO</div>
        <div>OR</div>
        <div>CONTACT@DRAVIMO.AE</div>
      </div>
      <div class="web">www.dravimo.ae</div>
      <div class="address">Dravimo LLC, Palm Crest Tower, Office 1304, Business</div>
    </div>
  </div>

  <div class="page cover">
    <div class="wordmark">DRAVIMO</div>
    <div class="motto">QUALITY IS NOT AN ACT, IT IS A HABIT</div>
    <div class="motto-source">- THEODOR VALE -</div>
    <div class="cover-photo" role="img" aria-label="Photo of a bright living room with white sofas, glass coffee table and grey rug"></div>
  </div>
</section>

<section class="spread spread--inside">
  <div class="page">
    <!-- design -->
    <div class="service-band" style="left:0;top:0;width:337px;height:250px;background:var(--lime)"></div>
    <div class="service-photo" role="img" aria-label="Photo of a bedroom with a white bed and tall curtains" style="left:154px;top:46px;width:183px;height:204px;background:linear-gradient(160deg,#ece6dc,#c9bba6 50%,#5a3a28)"></div>
    <div class="badge" style="left:213px;top:0">DRAVIMO</div>
    <div class="service-title" style="left:80px;top:25px;color:var(--rose)">DESIGN</div>
    <ul class="service-list service-list--left" style="right:183px;top:81px;color:#333">
      <li>Villas Interior Design</li><li>Villas Exterior Design</li><li>Landscape Design</li><li>Retail Interior Design</li><li>Office Interior Design</li><li>Hospitality Interior Design</li><li>Hotel Interior Design</li><li>Hotel Exterior Design</li><li>Restaurant Interior Design</li>
    </ul>
    <!-- landscaping -->
    <div class="service-band" style="left:0;top:250px;width:337px;height:226px;background:var(--rose)"></div>
    <div class="service-photo" role="img" aria-label="Photo of a bathroom with a corner tub and wrought iron window" style="left:154px;top:274px;width:183px;height:202px;background:linear-gradient(150deg,#e9c98f,#c98d4d 55%,#f1e4cc)"></div>
    <div class="badge" style="left:213px;top:235px">DRAVIMO</div>
    <div class="service-title" style="left:35px;top:253px;color:var(--landscape-title)">LANDSCAPING</div>
    <ul class="service-list service-list--left service-list--light" style="right:183px;top:320px;color:#fff">
      <li>Soft Landscaping</li><li>Irrigation Solutions</li><li>Hard land Scaping</li><li>External Lighting</li><li>Swimming Pool &amp;</li><li style="padding-right:25px" class="nodash">Water Features</li>
    </ul>
  </div>

  <div class="page">
    <!-- fitout -->
    <div class="service-band" style="left:0;top:0;width:337px;height:250px;background:var(--sky)"></div>
    <div class="service-photo" role="img" aria-label="Photo of a room with a wooden TV wall and light wood floor" style="left:0;top:46px;width:182px;height:204px;background:linear-gradient(180deg,#8a5a32,#b0804f 45%,#f1e3c6 65%,#e9d6b2)"></div>
    <div class="badge" style="left:44px;top:0">DRAVIMO</div>
    <div class="service-title" style="left:198px;top:25px;color:var(--fitout-title)">FITOUT</div>
    <ul class="service-list service-list--right" style="left:182px;top:81px;color:#333">
      <li class="dash">Development Approvals</li><li class="dash">Flooring Solutions</li><li class="dash">Partition</li><li class="dash">Sealing Solutions</li><li class="dash">MEP Works</li><li class="dash">Civil Works</li><li class="dash">Joinery</li><li class="dash">Glass and Aluminium</li><li>Works (subcontractor)</li>
    </ul>
    <!-- maintenance -->
    <div class="service-band" style="left:0;top:250px;width:337px;height:226px;background:var(--sun)"></div>
    <div class="service-photo" role="img" aria-label="Photo of a marble bathroom with glass shower and vanity" style="left:0;top:274px;width:182px;height:202px;background:linear-gradient(170deg,#d9d4cc,#b9a58a 45%,#6e5a48 80%,#8d7d6d)"></div>
    <div class="badge" style="left:44px;top:235px">DRAVIMO</div>
    <div class="service-title" style="left:198px;top:253px;color:var(--rose)">MAINTAINCE</div>
    <ul class="service-list service-list--right" style="left:182px;top:306px;color:#333">
      <li class="dash">AC Repair</li><li class="dash">Plumber Services</li><li class="dash">Electric Repair</li><li class="dash">Carpentry Work</li><li class="dash">Gypsum Ceiling</li><li class="dash">Painting Services</li><li class="dash">Cleaning Services</li><li class="dash">Emergency Services</li>
    </ul>
  </div>
</section>

<style>
  .service-list--left li.nodash::after { display: none; }
</style>
</body>
</html>
```